Ashcombe Vista Business Cards

We need business card designs for a modern home development, Ashcombe Vista. We would like to see modern looking designs- clean and simple but striking. I've attached some images of one of the homes so you can see the style of the homes we are putting on the market and perhaps they will inspire your design! I've also attached the logo- both horizontal and vertical. We need to use the logo on the card. I've also attached a sign that has a map of the development. If you can use that and still keep the card nice and clean, great. If not, it's not a problem to leave the map out completely.

```html
<!DOCTYPE html>
<html lang="en">
<head>
<meta charset="utf-8">
<title>Ashcombe Vista Business Cards</title>
<link rel="stylesheet" href="https://fonts.googleapis.com/css2?family=Exo+2:wght@400;500;700&display=swap">
<style>
  :root {
    --stage: #e9ebec;
    --card: #ffffff;
    --teal: #0a7f95;
    --ink: #2f3336;
    --ink-soft: #4a4f53;
    --on-teal: #ffffff;
  }
  * { box-sizing: border-box; margin: 0; padding: 0; }
  html, body { width: 1200px; height: 870px; overflow: hidden; }
  body {
    background: var(--stage);
    font-family: "Exo 2", sans-serif;
    display: flex;
    flex-direction: column;
    align-items: center;
    justify-content: center;
    gap: 34px;
  }
  .card {
    position: relative;
    width: 690px;
    height: 394px;
    background: var(--card);
    box-shadow: 0 6px 18px rgba(0,0,0,.18);
    overflow: hidden;
  }
  .brand-name {
    font-family: "Exo 2", sans-serif;
    font-weight: 700;
    color: var(--ink);
    text-transform: uppercase;
    letter-spacing: 1px;
    display: flex;
    align-items: center;
    gap: 8px;
  }
  .brand-mark {
    width: 14px; height: 14px;
    border-radius: 50%;
    background: var(--teal);
  }
  /* back */
  .card--back { display: flex; align-items: center; justify-content: center; }
  .card--back .brand-name { font-size: 30px; }
  /* front */
  .card--front .band {
    position: absolute;
    left: 0; right: 0; bottom: 0;
    height: 215px;
    background: var(--teal);
  }
  .contact-list {
    position: absolute;
    left: 120px; top: 26px;
    list-style: none;
    color: var(--ink-soft);
    font-size: 15px;
    letter-spacing: .5px;
  }
  .contact-list li { display: flex; align-items: center; gap: 10px; height: 28px; }
  .contact-list svg { width: 16px; height: 16px; fill: none; stroke: var(--ink); stroke-width: 1.8; }
  .card--front .brand-name {
    position: absolute;
    right: 28px; top: 138px;
    font-size: 18px;
  }
  .address {
    position: absolute;
    left: 40px; top: 214px;
    color: var(--on-teal);
    font-size: 20px;
    line-height: 30px;
    letter-spacing: .5px;
  }
  .person {
    position: absolute;
    right: 40px; bottom: 48px;
    text-align: right;
    color: var(--on-teal);
  }
  .person-name { font-size: 24px; font-weight: 500; letter-spacing: 1px; }
  .person-role { font-size: 18px; margin-top: 4px; letter-spacing: .5px; }
</style>
</head>
<body>
  <section class="card card--back">
    <div class="brand-name"><span class="brand-mark"></span>Ashcombe Vista</div>
  </section>

  <section class="card card--front">
    <ul class="contact-list">
      <li><svg viewBox="0 0 16 16"><path d="M4 1.5l2.5 3-1.5 1.5c1 2 3 4 5 5l1.5-1.5 3 2.5-2 2C7 13 3 9 2 3.5z"/></svg>014 555 0182</li>
      <li><svg viewBox="0 0 16 16"><rect x="4" y="1" width="8" height="14" rx="1.5"/><line x1="7" y1="12.5" x2="9" y2="12.5"/></svg>014 555 0183</li>
      <li><svg viewBox="0 0 16 16"><rect x="2" y="6" width="12" height="8"/><rect x="5" y="2" width="6" height="4"/></svg>014 555 0184</li>
      <li><svg viewBox="0 0 16 16"><rect x="1.5" y="3.5" width="13" height="9"/><path d="M1.5 3.5l6.5 5 6.5-5"/></svg>hello@ashcombevista.com</li>
      <li><svg viewBox="0 0 16 16"><circle cx="8" cy="8" r="6.5"/><ellipse cx="8" cy="8" rx="3" ry="6.5"/><line x1="1.5" y1="8" x2="14.5" y2="8"/></svg>www.ashcombevista.com</li>
    </ul>

    <div class="band"></div>

    <div class="brand-name"><span class="brand-mark"></span>Ashcombe Vista</div>

    <p class="address">204,12th floor,Harbor<br>Lane Road KLM</p>

    <div class="person">
      <p class="person-name">DANIEL WHITFORD</p>
      <p class="person-role">Managing Director</p>
    </div>
  </section>
</body>
</html>
```